Communication Skill: GLOW Bridge

I need a Design for a skill I teach to youth. That's why the title GLOW Bridge. GLOW stands for Thoughts, Emotions, Concerns, Hopes & Desires. Under each word are some examples that are meant to help people discuss certain things. I tried to create something myself but want something much more creative and dynamic. I have attached what I designed because it has the information I need in the design. Want it to have a techie look to it.

```html
<!DOCTYPE html>
<html lang="en">
<head>
<meta charset="utf-8">
<title>GLOW Bridge – Communication Skill</title>
<link rel="stylesheet" href="https://fonts.googleapis.com/css2?family=Poppins:wght@300;400&display=swap">
<style>
  :root {
    --brand-blue: #0a8fcb;
    --ink: #3a3a3a;
    --frame: #a8a8a8;
    --connector: #9a9a9a;
    --paper: #ffffff;
  }
  html, body {
    margin: 0;
    padding: 0;
    overflow: hidden;
    background: var(--paper);
  }
  .canvas {
    position: relative;
    width: 1200px;
    height: 848px;
    overflow: hidden;
    background: var(--paper);
    font-family: "Poppins", sans-serif;
    color: var(--ink);
  }
  .side-band {
    position: absolute;
    left: 0;
    top: 0;
    width: 128px;
    height: 848px;
    background: var(--brand-blue);
  }
  .side-band__title {
    position: absolute;
    left: 64px;
    top: 425px;
    transform: translate(-50%, -50%) rotate(-90deg);
    white-space: nowrap;
    margin: 0;
    color: #fff;
    font-weight: 300;
    font-size: 38px;
    letter-spacing: 0.16em;
  }
  .connectors {
    position: absolute;
    left: 0;
    top: 0;
  }
  .hub {
    position: absolute;
    left: 544px;
    top: 304px;
    width: 242px;
    height: 242px;
    border-radius: 50%;
    background: var(--brand-blue);
  }
  .card__header {
    position: absolute;
    width: 351px;
    height: 47px;
    border-radius: 7px;
    background: var(--brand-blue);
    color: #fff;
    display: flex;
    align-items: center;
    justify-content: center;
    margin: 0;
    font-weight: 400;
    font-size: 25px;
    letter-spacing: 0.2em;
  }
  .card__body {
    position: absolute;
    width: 351px;
    box-sizing: border-box;
    border: 1.5px solid var(--frame);
    border-radius: 8px;
    background: var(--paper);
    padding: 14px 26px 0;
    margin: 0;
    list-style: none;
    font-size: 20px;
    font-weight: 300;
  }
  .card__body li {
    height: 43px;
    line-height: 43px;
    white-space: nowrap;
    word-spacing: 0.15em;
  }
  .col-left { left: 172px; }
  .col-right { left: 807px; }
</style>
</head>
<body>
<main class="canvas">
  <aside class="side-band">
    <h1 class="side-band__title">GLOW BRIDGE</h1>
  </aside>

  <svg class="connectors" width="1200" height="848" viewBox="0 0 1200 848" aria-hidden="true">
    <g fill="none" stroke="var(--connector)" stroke-width="1.8" stroke-dasharray="5 4">
      <polyline points="402,302 402,419 516,419"/>
      <polyline points="658,274 658,161 775,161"/>
      <polyline points="812,429 929,429 929,509"/>
      <polyline points="670,575 670,690 553,690"/>
    </g>
    <g fill="#fff" stroke="var(--connector)" stroke-width="1.8">
      <circle cx="402" cy="295" r="8"/>
      <circle cx="524" cy="419" r="8"/>
      <circle cx="658" cy="282" r="8"/>
      <circle cx="782" cy="161" r="8"/>
      <circle cx="805" cy="429" r="8"/>
      <circle cx="929" cy="516" r="8"/>
      <circle cx="670" cy="567" r="8"/>
      <circle cx="546" cy="690" r="8"/>
    </g>
  </svg>

  <div class="hub" role="img" aria-label="Support agent wearing a headset icon"></div>

  <section class="card card--thoughts">
    <h2 class="card__header col-left" style="top:60px;">THOUGHTS</h2>
    <ul class="card__body col-left" style="top:124px;height:148px;">
      <li>It seems … I wonder …</li>
      <li>It’s my opinion … I believe …</li>
      <li>I assume … I think …</li>
    </ul>
  </section>

  <section class="card card--emotions">
    <h2 class="card__header col-right" style="top:60px;">EMOTIONS</h2>
    <ul class="card__body col-right" style="top:124px;height:191px;">
      <li>I’m … hopeful &nbsp;worried &nbsp;sad</li>
      <li>afraid &nbsp;mad &nbsp;glad &nbsp;happy</li>
      <li>confident &nbsp;insecure &nbsp;lonely</li>
      <li>bothered &nbsp;uncertain</li>
    </ul>
  </section>

  <section class="card card--concerns">
    <h2 class="card__header col-left" style="top:534px;">CONCERNS</h2>
    <ul class="card__body col-left" style="top:597px;height:195px;">
      <li>I worry about …</li>
      <li>I’m afraid that …</li>
      <li>I’m nervous because …</li>
      <li>It bothers me that …</li>
    </ul>
  </section>

  <section class="card card--hopes">
    <h2 class="card__header col-right" style="top:541px;">HOPES</h2>
    <ul class="card__body col-right" style="top:604px;height:188px;">
      <li>I hope … &nbsp;I wish …</li>
      <li>It’s my desire …</li>
      <li>I’d like to see … &nbsp;I want …</li>
      <li>I need …</li>
    </ul>
  </section>
</main>
</body>
</html>
```